CORAL HAVEN DENTAL
Family & Cosmetic Dentistry
Simple
Dr. Marisol Quint D.D.S., M.B.A.
Dentist
2435 Fenwick-Alder Road, Suite D-4
Sunnyvale, CA 94087
coralhavendental@mailvesto.com
______________has an appointment
With:_________________________
Date:_________________________
Time:_________________________
*Please call at least 48 hours in advance if you need to change or cancel this appointment.

```html
<!DOCTYPE html>
<html lang="en">
<head>
<meta charset="utf-8">
<title>Coral Haven Dental — Stationery Set</title>
<link href="https://fonts.googleapis.com/css2?family=Cinzel:wght@400;600&family=Open+Sans:wght@400;600&display=swap" rel="stylesheet">
<style>
  :root{
    --bg-dark:#1f1f1f;
    --bg-mid:#4a4a4a;
    --paper:#ffffff;
    --paper-shade:#eeeeee;
    --green-deep:#173a22;
    --green:#2f6a3c;
    --green-light:#4e8c58;
    --ink:#3a3a3a;
    --ink-soft:#8a8a8a;
    --mark-faint:#f1f1f1;
  }
  *{margin:0;padding:0;box-sizing:border-box}
  html,body{width:1200px;height:312px;overflow:hidden}
  body{
    position:relative;
    background:radial-gradient(ellipse at 55% 40%,var(--bg-mid) 0%,var(--bg-dark) 75%);
    font-family:"Open Sans",Arial,sans-serif;
    color:var(--ink);
  }
  .piece{position:absolute;background:var(--paper);box-shadow:0 2px 6px rgba(0,0,0,.45)}
  .brand-name{font-family:"Cinzel",Georgia,serif;font-weight:600;letter-spacing:.08em;color:var(--green);text-align:center;line-height:1.15}
  .brand-dot{display:block;margin:0 auto;border-radius:50%;background:var(--green)}

  /* Master logo */
  .master-logo{position:absolute;left:12px;top:14px;width:136px;text-align:center}
  .master-logo .brand-dot{width:30px;height:30px;background:var(--paper)}
  .master-logo .brand-name{color:var(--paper);font-size:15px;margin-top:8px}
  .master-logo .tagline{font-size:6px;color:#cfcfcf;margin-top:4px;letter-spacing:.05em}

  /* Business cards */
  .card{width:100px;height:58px}
  .card-front{left:8px;top:136px;display:flex;flex-direction:column;justify-content:center;padding:6px}
  .card-front .brand-dot{width:8px;height:8px}
  .card-front .brand-name{font-size:5.5px;margin-top:3px}
  .card-back{left:8px;top:202px;background:var(--paper);padding:5px;font-size:3.6px;color:var(--ink-soft)}
  .card-back p{margin-bottom:2px}
  .card-back .line{border-bottom:.5px solid #bbb;height:5px;margin-bottom:2px}
  .card-green{left:112px;top:202px;background:linear-gradient(135deg,var(--green-light),var(--green-deep));padding:6px;color:#e6efe7;font-size:3.6px;line-height:1.5}
  .card-green strong{display:block;font-size:4.4px}
  .card-contact{position:absolute;right:6px;top:4px;font-size:3px;color:var(--ink-soft);text-align:right;line-height:1.4}

  /* Letterheads */
  .letterhead{top:12px;width:212px;height:295px;padding:12px 14px}
  .letterhead-one{left:254px}
  .letterhead-two{left:490px}
  .letterhead .brand-dot{width:12px;height:12px}
  .letterhead .brand-name{font-size:6.5px;margin-top:3px}
  .letterhead .header{display:flex;justify-content:space-between;align-items:flex-start}
  .letterhead .contact{font-size:3.6px;line-height:1.5;color:var(--ink-soft);text-align:right}
  .letterhead-two .header{justify-content:center}
  .watermark{position:absolute;left:50%;top:50%;width:90px;height:90px;margin:-45px 0 0 -45px;border-radius:50%;background:var(--mark-faint)}
  .letterhead .footer{position:absolute;left:0;right:0;bottom:10px;text-align:center;font-size:3.6px;color:var(--ink-soft)}

  /* Flat envelopes */
  .envelope{width:196px;height:92px;padding:8px}
  .envelope-upper{left:704px;top:14px}
  .envelope-lower{left:704px;top:186px}
  .envelope .brand-dot{width:9px;height:9px;margin:0}
  .envelope .brand-name{font-size:5px;text-align:left;margin-top:2px}
  .envelope .return{font-size:3.4px;color:var(--ink-soft);margin-top:2px;line-height:1.4}

  /* Open envelope stack */
  .envelope-stack{position:absolute;left:922px;top:14px;width:272px;height:290px}
</style>
</head>
<body>

  <div class="master-logo">
    <span class="brand-dot"></span>
    <div class="brand-name">CORAL HAVEN<br>DENTAL</div>
    <div class="tagline">Family &amp; Cosmetic Dentistry</div>
  </div>

  <div class="piece card card-front">
    <span class="brand-dot"></span>
    <div class="brand-name">CORAL HAVEN DENTAL</div>
  </div>

  <div class="piece card card-back">
    <p>______________ has an appointment</p>
    <p>With:</p><div class="line"></div>
    <p>Date:</p><div class="line"></div>
    <p>Time:</p>
    <p>*Please call at least 48 hours in advance if you need to change or cancel this appointment.</p>
  </div>

  <div class="piece card card-green">
    <strong>Dr. Marisol Quint D.D.S., M.B.A.</strong>
    Dentist<br>
    2435 Fenwick-Alder Road, Suite D-4<br>
    Sunnyvale, CA 94087<br>
    coralhavendental@mailvesto.com
  </div>

  <div class="piece letterhead letterhead-one">
    <div class="header">
      <div>
        <span class="brand-dot"></span>
        <div class="brand-name">CORAL HAVEN<br>DENTAL</div>
      </div>
      <div class="contact">
        2435 Fenwick-Alder Road, Suite D-4<br>
        Sunnyvale, CA 94087<br>
        Tel (408) 555-0172<br>
        coralhavendental@mailvesto.com
      </div>
    </div>
    <div class="watermark"></div>
  </div>

  <div class="piece letterhead letterhead-two">
    <div class="header">
      <div>
        <span class="brand-dot"></span>
        <div class="brand-name">CORAL HAVEN<br>DENTAL</div>
      </div>
    </div>
    <div class="watermark"></div>
    <div class="footer">2435 Fenwick-Alder Road, Suite D-4 · Sunnyvale, CA 94087 · coralhavendental@mailvesto.com</div>
  </div>

  <div class="piece envelope envelope-upper">
    <span class="brand-dot"></span>
    <div class="brand-name">CORAL HAVEN DENTAL</div>
    <div class="return">2435 Fenwick-Alder Road, Suite D-4<br>Sunnyvale, CA 94087</div>
  </div>

  <div class="piece envelope envelope-lower">
    <span class="brand-dot"></span>
    <div class="brand-name">CORAL HAVEN DENTAL</div>
    <div class="return">2435 Fenwick-Alder Road, Suite D-4<br>Sunnyvale, CA 94087</div>
  </div>

  <svg class="envelope-stack" viewBox="0 0 272 290" aria-label="Three envelopes, open and closed">
    <defs>
      <linearGradient id="flap-green" x1="0" y1="0" x2="0" y2="1">
        <stop offset="0" stop-color="#173a22"/>
        <stop offset="1" stop-color="#3c7a48"/>
      </linearGradient>
    </defs>
    <!-- back envelope, flap open -->
    <polygon points="40,60 150,0 260,60" fill="url(#flap-green)"/>
    <rect x="40" y="60" width="220" height="90" fill="#ffffff"/>
    <polyline points="40,60 150,120 260,60" fill="none" stroke="#e2e2e2"/>
    <circle cx="150" cy="30" r="5" fill="#ffffff"/>
    <!-- middle envelope, flap open -->
    <polygon points="20,130 130,80 240,130" fill="#f4f4f4"/>
    <rect x="20" y="130" width="220" height="80" fill="#ffffff" stroke="#dddddd" stroke-width=".5"/>
    <circle cx="130" cy="112" r="5" fill="#2f6a3c"/>
    <!-- front envelope, flap closed -->
    <rect x="0" y="200" width="230" height="86" fill="#ffffff"/>
    <polygon points="0,200 115,250 230,200" fill="#f2f2f2" stroke="#dcdcdc" stroke-width=".5"/>
    <polygon points="100,243 115,250 130,243 115,236" fill="#173a22"/>
  </svg>

</body>
</html>
```